WordPress Design for both website and landing page for an expert

I need a clean and stylish design for my new website. I work as an expert (see attached file WHY HOW WHAT), my product is expert opinion (reports) for company evaluations You can use all of the attached pictures colored or black / white. The person is me, you can add other pictures, if you want. The design should be clean and stylish, so you could use white, black, gray, silver and / or one additional color. I have added an idea about my website, see attached file CONCEPT WEBSITE If you have any more information, please do not hesitate to contact us 'Hesitate to ask me ...

```html
<!DOCTYPE html>
<html lang="en">
<head>
<meta charset="utf-8">
<title>Milo Varek — Why / How I Do</title>
<link href="https://fonts.googleapis.com/css2?family=Montserrat:wght@400;500;600&family=Noto+Serif:wght@400&display=swap" rel="stylesheet">
<style>
  :root {
    --ink: #2a2f36;
    --heading: #333a44;
    --body: #8a95a3;
    --muted: #9aa1a9;
    --line: #b9bec4;
    --soft: #eef1f4;
    --footer: #f1f3f5;
    --white: #ffffff;
    --photo-a: #e9eef3;
    --photo-b: #c9d6e2;
    --photo-c: #7fb1d8;
  }
  * { box-sizing: border-box; margin: 0; padding: 0; }
  html, body { width: 999px; height: 1200px; overflow: hidden; background: var(--white); }
  body { position: relative; font-family: 'Montserrat', Arial, sans-serif; color: var(--ink); }

  .site-header { position: absolute; top: 0; left: 0; width: 999px; height: 110px; }
  .brand { position: absolute; left: 56px; top: 64px; display: flex; align-items: center; gap: 10px; }
  .brand-square { width: 14px; height: 14px; background: var(--ink); }
  .brand-name { font-size: 15px; font-weight: 400; letter-spacing: 2.5px; color: var(--ink); text-transform: uppercase; }

  .main-nav { position: absolute; top: 50px; right: 57px; display: flex; gap: 28px; }
  .main-nav a { font-size: 11px; font-weight: 500; letter-spacing: 1.6px; color: var(--ink); text-decoration: none; text-transform: uppercase; }
  .main-nav a.is-current { color: var(--muted); }

  .hero-photo { position: absolute; left: 114px; top: 164px; width: 386px; height: 314px;
    background: linear-gradient(160deg, var(--photo-a) 0%, var(--photo-b) 55%, var(--photo-c) 100%); }
  .hero-title { position: absolute; left: 250px; top: 278px; width: 500px; text-align: center;
    font-size: 35px; font-weight: 500; letter-spacing: 3px; line-height: 42px; color: var(--heading); text-transform: uppercase; }

  .copy { font-family: 'Noto Serif', Georgia, serif; font-size: 12.5px; line-height: 21.5px; color: var(--body); }
  .intro { position: absolute; left: 235px; top: 531px; width: 540px; }
  .section-title { position: absolute; left: 235px; top: 640px; font-size: 22px; font-weight: 500; color: var(--ink); }
  .section-lead { position: absolute; left: 235px; top: 679px; width: 400px; }

  .feature { position: absolute; top: 772px; width: 245px; }
  .feature-one { left: 235px; }
  .feature-two { left: 528px; }
  .feature-icon { width: 108px; height: 108px; border-radius: 50%; background: var(--soft); }
  .feature .copy { margin-top: 24px; }

  .cta { position: absolute; left: 235px; top: 1052px; width: 179px; height: 34px; border: 1px solid var(--line);
    border-radius: 17px; display: flex; align-items: center; justify-content: center;
    font-size: 10.5px; font-weight: 600; letter-spacing: 1px; color: var(--ink); text-decoration: none; text-transform: uppercase; }

  .site-footer { position: absolute; left: 0; top: 1143px; width: 999px; height: 57px; background: var(--footer); }
  .copyright { position: absolute; left: 114px; top: 23px; font-size: 9.5px; color: #7b838c; }
  .social { position: absolute; top: 7px; left: 759px; display: flex; gap: 2px; }
  .social span { width: 42px; height: 42px; border-radius: 50%; background: var(--white); display: block; }
</style>
</head>
<body>
  <header class="site-header">
    <div class="brand"><span class="brand-square"></span><span class="brand-name">Milo Varek</span></div>
    <nav class="main-nav">
      <a href="#">Home</a>
      <a href="#">About</a>
      <a href="#">What I do</a>
      <a href="#" class="is-current">Why / How I do</a>
      <a href="#">Contact</a>
    </nav>
  </header>

  <div class="hero-photo" role="img" aria-label="Photo of hands pointing at a printed bar chart report on a desk"></div>
  <h1 class="hero-title">Economy is my<br>passion</h1>

  <p class="copy intro">Economy is made in numbers. Sometimes it is difficult to find the right numbers. I am always interested in finding out, how economy works and which numbers will tell the really true story. I want to know it ...</p>

  <h2 class="section-title">How I do?</h2>
  <p class="copy section-lead">Each report begins with understanding. So I ask you questions and listen very carefully.</p>

  <div class="feature feature-one">
    <div class="feature-icon" role="img" aria-label="Icon of a report with chart and magnifying glass"></div>
    <p class="copy">In the preparation of each report I follow one defined&nbsp; process, but which is tailored to the particular each company is customized.</p>
  </div>
  <div class="feature feature-two">
    <div class="feature-icon" role="img" aria-label="Icon of a calculator and invoice with a dollar sign"></div>
    <p class="copy">This approach, coupled with specialization in the area business valuation, allows orders very fast &amp; at the same time&nbsp; correct and impeccable handle</p>
  </div>

  <a class="cta" href="#">Contact now!</a>

  <footer class="site-footer">
    <p class="copyright">Copyright © 2018 Milo Varek. All Rights Reserved</p>
    <div class="social" aria-label="Social links">
      <span></span><span></span><span></span>
    </div>
  </footer>
</body>
</html>
```